Bramwell Garden Maintenance - Needs a business card! Easy JOB!

I need a business card for a new company called Bramwell Garden Maintenance. I will be offering the below services.

I am relatively open for ideas, so please be at your creative best.

I think I will list all the services offered on the rear of the card.

- Gardening
- Lawn Care
- Hedge Trimming
- Rubbish Removal
- Weeding/Spraying
- Landscaping
- Gutter Cleaning
- Solar Panel Cleaning
- Irrigation
- Pruning
- On-Site Mulching
- Ask for other services

I am still a little undecided on the colours. I prefer the logos with the Blue text, but I am open for ideas ( the logo/texts colours are not final).

Please use the catch phrase "What can Bramwell do for you?"

Here are the required details.

Bramwell Garden Maintenance

Neil Harcourt (owner)
Ph: 1300 XXX XXX
Mob: 0427 XXX XXX

neil@bramwellgarden.com.au
www.bramwellgarden.com.au
facebook.com/BramwellGarden
twitter.com/BramwellGarden
ABN: XXX XXX XXX ( this can be in smaller text somewhere, this is the least important )

Thankyou in advance! And good luck.

regards,
Neil
Updates

Hi everyone, please make sure you include the phrase "What can Bramwell do for you?" on the designs.

thanks,
Neil

Definitely liking the focus on a majority of the design on the blue colour from the logo. Also a splash of green in the plant.

Please make sure you list the services provided on the rear of the card. thanks.

With the service listing, please make "ask for other services" stand out, either a different colour or position or size... as long as it is more noticeable than the other services listed. Thanks.

Industry/Entity Type

Business

Requirements
Must have
• - use the font supplied (Brandon Family Font)
- use of the catch phrase "What can Bramwell do for you?"
- Double sided design
- Facebook and Twitter logos/links
- Please use symbol/picture for "phone" "mobile" "email" instead of using the words.
- List the services provided on the rear of the card

```html
<!DOCTYPE html>
<html lang="en">
<head>
<meta charset="utf-8">
<title>Bramwell Garden Maintenance – Business Card</title>
<link rel="stylesheet" href="https://fonts.googleapis.com/css2?family=Montserrat:wght@600;700&family=Open+Sans:wght@400;600;700&display=swap">
<style>
  :root{
    --page:#e9eaeb;
    --card-light-top:#f7f7f8;
    --card-light-bottom:#e4e5e7;
    --slate:#3f4d57;
    --slate-edge:#5c6871;
    --brand-blue:#1f5fb8;
    --tagline:#7a8187;
    --text-light:#ffffff;
    --muted-light:#e3e7ea;
  }
  *{box-sizing:border-box;margin:0;padding:0}
  html,body{width:1200px;height:1000px;overflow:hidden}
  body{background:var(--page);position:relative;font-family:"Open Sans",Arial,sans-serif}

  .card{position:absolute;width:827px;height:464px;overflow:hidden;box-shadow:0 4px 14px rgba(0,0,0,.18)}
  .card--front{left:53px;top:23px;background:linear-gradient(var(--card-light-top),var(--card-light-bottom))}
  .card--back{left:325px;top:507px;background:var(--slate)}

  /* brand block */
  .brand{position:absolute;left:0;right:0;text-align:center}
  .brand__mark{display:block;margin:0 auto 20px;width:110px;height:110px;border-radius:50%;background:var(--brand-blue)}
  .brand__name{font-family:"Montserrat",Arial,sans-serif;font-weight:700;color:var(--brand-blue);line-height:1.1;letter-spacing:.3px}

  .card--front .brand{top:77px}
  .card--front .brand__name{font-size:34px}
  .tagline{position:absolute;left:0;right:0;top:298px;text-align:center;font-family:"Open Sans",Arial,sans-serif;font-weight:700;font-size:19px;color:var(--tagline)}

  .services{position:absolute;left:0;right:0;bottom:0;height:107px;background:var(--slate);border-top:8px solid var(--slate-edge);padding:18px 0 0 32px;display:grid;grid-template-columns:233px 176px 200px auto}
  .services ul{list-style:none}
  .services li{color:var(--text-light);font-size:15.5px;line-height:19.5px}

  /* back */
  .contact{position:absolute;left:0;top:0;width:495px;height:100%;padding:90px 0 0 47px;color:var(--text-light)}
  .contact__name{font-family:"Montserrat",Arial,sans-serif;font-weight:700;font-size:29px;line-height:1.05}
  .contact__role{font-size:19px;color:var(--muted-light);line-height:1.2;margin-bottom:14px}
  .contact__list{list-style:none;font-size:15px;line-height:21px}
  .contact__list li{display:flex;align-items:center}
  .contact__list .icon{width:16px;height:16px;margin:0 8px 0 24px;flex:none}
  .contact__list .dot{width:14px;height:14px;border-radius:50%;background:var(--text-light);margin:0 9px 0 25px;flex:none}
  .contact__abn b{font-weight:700}
  .contact__gap{height:21px}
  .contact__company{font-weight:700;font-size:15px;margin-top:8px}
  .contact__address{font-size:15px;line-height:21px}

  .logo-panel{position:absolute;right:0;top:0;width:317px;height:100%;background:linear-gradient(var(--card-light-top),var(--card-light-bottom));border-left:13px solid var(--slate-edge)}
  .logo-panel .brand{top:116px}
  .logo-panel .brand__mark{width:96px;height:96px;margin-bottom:22px}
  .logo-panel .brand__name{font-size:26px;padding:0 20px}
</style>
</head>
<body>

<section class="card card--front">
  <div class="brand">
    <span class="brand__mark"></span>
    <div class="brand__name">Bramwell Garden Maintenance</div>
  </div>
  <p class="tagline">What can Bramwell do for you?</p>
  <div class="services">
    <ul><li>Gardening</li><li>Lawn Care</li><li>Hedge Trimming</li></ul>
    <ul><li>Rubbish Removal</li><li>Weeding/Spraying</li><li>Landscaping</li></ul>
    <ul><li>Gutter Cleaning</li><li>Solar Panel Cleaning</li><li>Irrigation</li></ul>
    <ul><li>Pruning</li><li>On-Site Mulching</li><li class="services__more">Ask for other services</li></ul>
  </div>
</section>

<section class="card card--back">
  <div class="contact">
    <h1 class="contact__name">Neil Harcourt</h1>
    <p class="contact__role">Owner</p>
    <ul class="contact__list">
      <li><svg class="icon" viewBox="0 0 16 16" aria-hidden="true"><path fill="#fff" d="M4 1.5l2.3 3-1.4 1.6c.8 1.8 2.2 3.3 4 4.1l1.6-1.4 3 2.3-1.3 2.5C7 13.4 2.6 9 2.2 2.8z"/></svg>1300 482 190</li>
      <li><svg class="icon" viewBox="0 0 16 16" aria-hidden="true"><rect x="4" y="1.5" width="8" height="4" fill="#fff"/><rect x="1.5" y="6" width="13" height="6" rx="1" fill="#fff"/><rect x="4" y="10" width="8" height="4.5" fill="#fff" stroke="#3f4d57" stroke-width="1"/></svg>44 5120 7736</li>
      <li><svg class="icon" viewBox="0 0 16 16" aria-hidden="true"><rect x="5" y="2" width="7" height="12.5" rx="1" fill="#fff"/><rect x="6.2" y="3.6" width="4.6" height="7" fill="#3f4d57"/></svg>632 918 4402</li>
      <li class="contact__abn"><b>ABN:</b>&nbsp;51 302 664 917</li>
      <li class="contact__gap"></li>
      <li><span class="dot"></span>linkvale.com/BramwellGarden</li>
      <li><span class="dot"></span>chirpnest.com/BramwellGarden</li>
      <li class="contact__gap"></li>
      <li><svg class="icon" viewBox="0 0 16 16" aria-hidden="true"><rect x="1" y="3.5" width="14" height="9.5" fill="#fff"/><path d="M1.5 4l6.5 5 6.5-5" fill="none" stroke="#3f4d57" stroke-width="1.3"/></svg>neil@bramwellgarden.com.au</li>
      <li><svg class="icon" viewBox="0 0 16 16" aria-hidden="true"><g fill="none" stroke="#fff" stroke-width="1.3"><circle cx="8" cy="8" r="6.3"/><ellipse cx="8" cy="8" rx="2.8" ry="6.3"/><path d="M1.7 8h12.6M2.8 4.8h10.4M2.8 11.2h10.4"/></g></svg>www.bramwellgarden.com.au</li>
    </ul>
    <p class="contact__company">Bramwell Garden Maintenance</p>
    <p class="contact__address">218 Harbour Lane west, Kellsford, ST 40817</p>
  </div>
  <div class="logo-panel">
    <div class="brand">
      <span class="brand__mark"></span>
      <div class="brand__name">Bramwell Garden Maintenance</div>
    </div>
  </div>
</section>

</body>
</html>
```